Informational Website for MOSVALEK-MOSaic VALley Eastern Kinship of Clinic Record Scholars

I need an informational website to help establish us as a legitimate entity. This will help us as we seek funding in to perform the research we intend to carry out. We are a newly formed group of family physicians and primary care researchers from 9 different countries around the world. We have access to electronic medical record data and/or health insurance claims data in our respective countries. We intend to perform international comparative studies in primary care. Our set of projects are to study the impact of the COVID-19 pandemic on primary care in our respective countries and around the world.
I've already purchased a domain and website from Wix. It is a premium account. The domain is https://www.mosvalekclinicnet.org

Target Market(s)

Researchers, policy makers, universities, research funding agencies

Coding

Coded - Design and coding required

Number of Pages Required

5+ page

Font styles to use
Sans Serif

Requirements
Must have
• Must have our logo and an interactive map of the world highlighting Canada, Australia, China (including Hong Kong), Norway, Singapore, South Korea, Sweden, United Kingdom, United States.
This map must be editable such that we can add or remove countries and cities as we evolve. Please see attached brief.
Nice to have
• Nice to depict primary care and big data research

```html
<!DOCTYPE html>
<html lang="en">
<head>
<meta charset="utf-8">
<title>MOSVALEK – MOSaic VALley Eastern Kinship of Clinic Record Scholars</title>
<link rel="stylesheet" href="https://fonts.googleapis.com/css2?family=Montserrat:wght@700&family=Roboto+Condensed:wght@400;700&family=Roboto:wght@400;500&display=swap">
<style>
:root{
  --green:#80aa00;
  --green-dark:#6f9500;
  --blue:#0c3a84;
  --blue-deep:#082c6a;
  --white:#ffffff;
  --ink:#333333;
  --field:#e9e9e9;
  --placeholder:#7a7a7a;
}
*{margin:0;padding:0;box-sizing:border-box}
html,body{width:1200px;height:2887px;overflow:hidden;background:var(--white)}
body{font-family:"Roboto",Arial,sans-serif;color:var(--ink)}
.page{position:relative;width:1200px;height:2887px;overflow:hidden}
.abs{position:absolute}

/* header */
.top-line{left:0;top:0;width:1200px;height:3px;background:var(--green)}
.site-header{left:0;top:3px;width:1200px;height:99px;background:var(--white)}
.brand{left:92px;top:0;width:182px;height:151px;background:var(--white);z-index:3;display:flex;flex-direction:column;align-items:center;justify-content:center;gap:10px}
.brand-mark{width:46px;height:46px;border-radius:50%;background:var(--green)}
.brand-name{font-family:"Montserrat",sans-serif;font-weight:700;font-size:25px;color:var(--blue);letter-spacing:.5px}
.main-nav{left:540px;top:40px;display:flex;gap:32px;font-size:14.5px;color:#222}
.main-nav a{color:inherit;text-decoration:none;padding-bottom:10px}
.main-nav a.active{color:var(--green);border-bottom:2px solid var(--green)}
.login{left:946px;top:30px;width:142px;height:46px;border:2px solid var(--green);border-radius:23px;display:flex;align-items:center;justify-content:center;gap:5px;color:var(--green);font-weight:500;font-size:14px}

/* hero */
.hero-visual{left:0;top:102px;width:1200px;height:580px;background:linear-gradient(100deg,#cfd8e2 0%,#e6ecf2 35%,#f2f4f6 60%,#cdd6de 100%)}
.hero-band{left:0;top:537px;width:1200px;height:145px;background:linear-gradient(90deg,rgba(12,58,132,.88) 0%,rgba(70,110,110,.85) 45%,rgba(128,170,0,.9) 100%);text-align:center;color:var(--white)}
.hero-title{font-family:"Roboto",sans-serif;font-weight:400;font-size:44px;letter-spacing:1px;margin-top:24px;line-height:50px}
.hero-sub{font-family:"Roboto Condensed",sans-serif;font-size:29px;line-height:36px;margin-top:4px}

/* feature cards */
.card{top:757px;width:308px;height:404px;color:var(--white);text-align:center;padding-top:16px}
.card-1{left:111px;background:var(--blue);border-radius:0 40px 40px 0}
.card-2{left:446px;background:linear-gradient(180deg,var(--green) 0%,#6a9a10 35%,var(--blue) 95%);border-radius:40px}
.card-3{left:781px;background:var(--blue);border-radius:40px 0 0 40px}
.card-icon{width:93px;height:93px;border-radius:50%;margin:0 auto;display:flex;align-items:center;justify-content:center}
.icon-green{background:var(--green)}
.icon-blue{background:var(--blue)}
.card h3{font-family:"Roboto Condensed",sans-serif;font-weight:700;font-size:22px;margin-top:22px;line-height:28px}
.card p{font-size:14.5px;line-height:21.5px;margin:15px 40px 0}
.btn{display:inline-flex;align-items:center;justify-content:center;font-family:"Roboto Condensed",sans-serif;font-weight:700;font-size:15px;color:var(--white);text-transform:uppercase}
.card .btn{width:172px;height:50px;background:var(--green);margin-top:22px}

/* about */
.bands{left:0;top:0}
.about{left:0;top:1310px;width:1200px;text-align:center;color:var(--white)}
.about h2{font-family:"Montserrat",sans-serif;font-weight:700;font-size:46px;line-height:56px}
.about h3{font-family:"Roboto Condensed",sans-serif;font-weight:700;font-size:30px;line-height:36px;margin-top:-4px}
.about p{font-size:14px;line-height:22.4px;margin:22px auto 0;width:760px}
.about p + p{margin-top:16px}
.about .btn{width:172px;height:50px;background:var(--blue);margin-top:40px}

/* map */
.world-map{left:185px;top:1865px;width:832px;height:437px;background:radial-gradient(ellipse at 50% 45%,rgba(235,238,242,.95) 0%,rgba(220,226,234,.85) 55%,rgba(200,210,225,.25) 80%,rgba(12,58,132,0) 100%);border-radius:40%}
.pin{width:12px;height:16px}
.map-tip{left:664px;top:2085px;width:253px;height:65px;background:var(--white);border-radius:32px;font-size:8px;line-height:12px;color:#333;text-align:center;padding:14px 22px 0}
.tip-badge{left:773px;top:2055px;width:34px;height:34px;border-radius:50%;background:var(--white);border:2px solid var(--green)}

/* contact */
.contact-title{left:0;top:2338px;width:1200px;text-align:center;font-family:"Montserrat",sans-serif;font-weight:700;font-size:47px;color:var(--white)}
.contact-item{top:2400px;display:flex;align-items:center;gap:10px;color:var(--white);font-family:"Roboto Condensed",sans-serif;font-weight:700;font-size:15.5px;line-height:25px}
.contact-icon{width:49px;height:49px;border-radius:50%;background:var(--green);display:flex;align-items:center;justify-content:center;flex:none}
.field{background:var(--field);color:var(--placeholder);font-size:16px;padding:0 18px;display:flex;align-items:center}
.field-message{align-items:flex-start;padding-top:14px}
.submit{left:531px;top:2760px;width:138px;height:47px;background:var(--green)}
.copyright{left:0;top:2842px;width:1200px;text-align:center;color:var(--white);font-family:"Roboto Condensed",sans-serif;font-size:16px}
</style>
</head>
<body>
<div class="page">

  <div class="abs top-line"></div>
  <header class="abs site-header"></header>
  <div class="abs brand">
    <span class="brand-mark"></span>
    <span class="brand-name">MOSVALEK</span>
  </div>
  <nav class="abs main-nav">
    <a class="active">Home</a><a>About</a><a>Services</a><a>Clients</a><a>Contact</a>
  </nav>
  <div class="abs login">
    <svg width="14" height="14" viewBox="0 0 14 14" fill="none" stroke="currentColor" stroke-width="1.5"><circle cx="7" cy="7" r="6"/><circle cx="7" cy="5.5" r="2"/><path d="M3.5 11.2c1-1.8 6-1.8 7 0"/></svg>
    LOG IN
  </div>

  <div class="abs hero-visual" role="img" aria-label="Photo of a senior researcher in a lab coat working with samples in a bright laboratory"></div>
  <div class="abs hero-band">
    <div class="hero-title">MOSVALEK</div>
    <div class="hero-sub">MOSAIC VALLEY EASTERN KINSHIP OF CLINIC RECORD SCHOLARS</div>
  </div>

  <section class="abs card card-1">
    <div class="card-icon icon-green">
      <svg width="50" height="46" viewBox="0 0 50 46" fill="none" stroke="#fff" stroke-width="2"><rect x="4" y="4" width="42" height="28" rx="2"/><path d="M18 40h14M25 32v8"/><path d="M20 14l-5 4 5 4M30 14l5 4-5 4M27 12l-4 12"/></svg>
    </div>
    <h3>Primary care researchers</h3>
    <p>Sed ut perspiciatis unde omnis iste natus error sit voluptatem accusantium doloremque laudantium, totam rem aperiam, eaque ipsa quae ab illo inventore veritatis et quasi architecto beatae vitae</p>
    <span class="btn">More info</span>
  </section>
  <section class="abs card card-2">
    <div class="card-icon icon-blue">
      <svg width="50" height="50" viewBox="0 0 50 50" fill="none" stroke="#fff" stroke-width="2"><rect x="8" y="10" width="36" height="12" rx="6"/><path d="M14 22v16a4 4 0 0 0 8 0V22"/><circle cx="30" cy="16" r="2"/><circle cx="37" cy="16" r="2"/></svg>
    </div>
    <h3>Electronic medical record</h3>
    <p>Sed ut perspiciatis unde omnis iste natus error sit voluptatem accusantium doloremque laudantium, totam rem aperiam, eaque ipsa quae ab illo inventore veritatis et quasi architecto beatae vitae</p>
    <span class="btn">More info</span>
  </section>
  <section class="abs card card-3">
    <div class="card-icon icon-green">
      <svg width="50" height="50" viewBox="0 0 50 50" fill="none" stroke="#fff" stroke-width="2"><circle cx="25" cy="25" r="14"/><path d="M25 5v5M25 40v5M5 25h5M40 25h5M11 11l4 4M35 35l4 4M39 11l-4 4M11 39l4-4"/><path d="M18 25h14M28 21l4 4-4 4"/></svg>
    </div>
    <h3>Health insurance claims data</h3>
    <p>Sed ut perspiciatis unde omnis iste natus error sit voluptatem accusantium doloremque laudantium, totam rem aperiam, eaque ipsa quae ab illo inventore veritatis et quasi architecto beatae vitae</p>
    <span class="btn">More info</span>
  </section>

  <svg class="abs bands" width="1200" height="2887" viewBox="0 0 1200 2887" aria-hidden="true">
    <defs>
      <linearGradient id="deepBlue" x1="0" y1="0" x2="0" y2="1">
        <stop offset="0" stop-color="#0c3a84"/>
        <stop offset="1" stop-color="#0a3279"/>
      </linearGradient>
    </defs>
    <rect x="0" y="1700" width="1200" height="1187" fill="url(#deepBlue)"/>
    <path d="M0 1322 Q600 1186 1200 1322 L1200 1764 Q600 1898 0 1764 Z" fill="#80aa00"/>
  </svg>

  <section class="abs about">
    <h2>ABOUT US</h2>
    <h3>MOSaic VALley Eastern Kinship of Clinic Record Scholars</h3>
    <p>We are family physicians and primary care researchers from 9 different countries around the world. We have access to electronic medical record data and/or health insurance claims data in our respective countries. We intend to perform international comparative studies in primary care. Our first project is to study the impact of the COVID-19 pandemic on primary care in our respective countries and around the world.</p>
    <p>Lorem ipsum dolor sit amet, consectetur adipiscing elit, sed do eiusmod tempor incididunt ut labore et dolore magna aliqua. Ut enim ad minim veniam, quis nostrud exercitation ullamco laboris nisi ut aliquip ex ea commodo consequat. Duis aute irure dolor in reprehenderit in voluptate velit esse cillum dolore eu fugiat nulla pariatur. Excepteur sint occaecat cupidatat non proident, sunt in culpa qui officia deserunt mollit anim id est laborum.Lorem ipsum dolor sit amet, consectetur adipiscing elit, sed do eiusmod tempor incididunt ut labore et dolore magna aliqua. Ut enim ad minim veniam, quis nostrud exercitation ullamco laboris nisi ut aliquip ex ea commodo consequat. Duis aute irure dolor</p>
    <span class="btn">Read more</span>
  </section>

  <div class="abs world-map" role="img" aria-label="World map in light grey highlighting member countries with red location pins"></div>
  <svg class="abs pin" style="left:340px;top:2025px" viewBox="0 0 12 16"><path d="M6 0a6 6 0 0 1 6 6c0 4-6 10-6 10S0 10 0 6a6 6 0 0 1 6-6z" fill="#e02020"/><circle cx="6" cy="6" r="2" fill="#fff"/></svg>
  <svg class="abs pin" style="left:553px;top:1970px" viewBox="0 0 12 16"><path d="M6 0a6 6 0 0 1 6 6c0 4-6 10-6 10S0 10 0 6a6 6 0 0 1 6-6z" fill="#e02020"/><circle cx="6" cy="6" r="2" fill="#fff"/></svg>
  <svg class="abs pin" style="left:588px;top:1935px" viewBox="0 0 12 16"><path d="M6 0a6 6 0 0 1 6 6c0 4-6 10-6 10S0 10 0 6a6 6 0 0 1 6-6z" fill="#e02020"/><circle cx="6" cy="6" r="2" fill="#fff"/></svg>
  <svg class="abs pin" style="left:622px;top:1925px" viewBox="0 0 12 16"><path d="M6 0a6 6 0 0 1 6 6c0 4-6 10-6 10S0 10 0 6a6 6 0 0 1 6-6z" fill="#e02020"/><circle cx="6" cy="6" r="2" fill="#fff"/></svg>
  <svg class="abs pin" style="left:784px;top:2040px" viewBox="0 0 12 16"><path d="M6 0a6 6 0 0 1 6 6c0 4-6 10-6 10S0 10 0 6a6 6 0 0 1 6-6z" fill="#e02020"/><circle cx="6" cy="6" r="2" fill="#fff"/></svg>
  <svg class="abs pin" style="left:862px;top:2020px" viewBox="0 0 12 16"><path d="M6 0a6 6 0 0 1 6 6c0 4-6 10-6 10S0 10 0 6a6 6 0 0 1 6-6z" fill="#e02020"/><circle cx="6" cy="6" r="2" fill="#fff"/></svg>
  <svg class="abs pin" style="left:934px;top:1965px" viewBox="0 0 12 16"><path d="M6 0a6 6 0 0 1 6 6c0 4-6 10-6 10S0 10 0 6a6 6 0 0 1 6-6z" fill="#e02020"/><circle cx="6" cy="6" r="2" fill="#fff"/></svg>
  <svg class="abs pin" style="left:905px;top:2197px" viewBox="0 0 12 16"><path d="M6 0a6 6 0 0 1 6 6c0 4-6 10-6 10S0 10 0 6a6 6 0 0 1 6-6z" fill="#e02020"/><circle cx="6" cy="6" r="2" fill="#fff"/></svg>
  <div class="abs map-tip">https://www.mosvalekclinicnet.org/en/Our-Team/Academic-Staff/Dr-Lena-Orvik-Haldane/profile</div>
  <div class="abs tip-badge"></div>

  <h2 class="abs contact-title">CONTACT US</h2>
  <div class="abs contact-item" style="left:174px">
    <span class="contact-icon"><svg width="14" height="18" viewBox="0 0 12 16"><path d="M6 0a6 6 0 0 1 6 6c0 4-6 10-6 10S0 10 0 6a6 6 0 0 1 6-6z" fill="#fff"/><circle cx="6" cy="6" r="2" fill="#80aa00"/></svg></span>
    <span>123, Lorem ipsum dolor sit<br>amet, consectetur</span>
  </div>
  <div class="abs contact-item" style="left:498px">
    <span class="contact-icon"><svg width="16" height="12" viewBox="0 0 16 12"><rect width="16" height="12" rx="1" fill="#fff"/><path d="M0 1l8 6 8-6" fill="none" stroke="#80aa00" stroke-width="1.5"/></svg></span>
    <span>Mail us :<br>info@companyname.com</span>
  </div>
  <div class="abs contact-item" style="left:843px">
    <span class="contact-icon"><svg width="16" height="16" viewBox="0 0 16 16"><path d="M3.5 1l2.5 3-1.5 2c1 2 3 4 5 5l2-1.5 3 2.5-1.5 2.5C8 15 1 8 1 2.5z" fill="#fff"/></svg></span>
    <span>Call us :<br>+1 888 888 8888</span>
  </div>

  <div class="abs field" style="left:338px;top:2483px;width:253px;height:47px">Enter Your Name</div>
  <div class="abs field" style="left:608px;top:2483px;width:253px;height:47px">Enter Your Email</div>
  <div class="abs field" style="left:338px;top:2545px;width:523px;height:47px">Enter Your Subject</div>
  <div class="abs field field-message" style="left:338px;top:2606px;width:523px;height:135px">Type your message here</div>
  <span class="abs btn submit">Submit</span>

  <p class="abs copyright">© Copyrights 2020 Company Name | All Rights Reserved</p>
</div>
</body>
</html>
```